Computer Company needs a Business card design

We need a business card design for our business. We assist people to transition to the QLX (Quorra Linkwave Exchange). The Australian Government-owned qlx™ network is a brand new telecommunications network currently being rolled out across Australia, giving access to a reliable broadband connection. Our niche market will predominantly be domestic customers in the 50+ age bracket. The assistance that we provide is everything from arranging the equipment, arranging the plan and contract term, appointment times, final testing of the network and any tweaks that need to be made. We basically PM the transition from start to finish. The business card design should be minimalist, should communicate loyalty and stability, should be easy to read and clearly explain what we do. We have asked for front and back. However, the back of the card does not have to include much information at all. It could be just a small design, or a repeat of our phone number. Up to you. The attached file only says what is required on the card. It does not specify where to arrange the text, what fonts to use, etc etc. As much as we would like to give you more info, due to our very limited design ability, we are not really able to send you any rough, or otherwise, designs of what we are after. Hopefully the above description is enough for you.

```html
<!DOCTYPE html>
<html lang="en">
<head>
<meta charset="utf-8">
<title>Hartwell Connect Business Card</title>
<link href="https://fonts.googleapis.com/css2?family=Montserrat:wght@400;500;600&display=swap" rel="stylesheet">
<style>
  :root {
    --stage: #262626;
    --brand-blue: #1479c6;
    --brand-blue-light: #1b93d2;
    --brand-sky: #1a9ad8;
    --ink-blue: #1565b8;
    --text-grey: #555a60;
    --muted-grey: #8a8f95;
    --rule-blue: #7fb6e0;
    --paper: #ffffff;
  }
  * { margin: 0; padding: 0; box-sizing: border-box; }
  html, body { width: 1200px; height: 900px; overflow: hidden; }
  body {
    background: var(--stage);
    font-family: "Montserrat", Arial, sans-serif;
    position: relative;
  }
  .card {
    position: absolute;
    left: 290px;
    width: 620px;
    height: 354px;
    border-radius: 26px;
    overflow: hidden;
    box-shadow: 0 14px 30px rgba(0,0,0,0.45);
  }
  .card-front {
    top: 70px;
    background: radial-gradient(ellipse at 65% 60%, var(--brand-blue-light) 0%, var(--brand-blue) 70%);
    display: flex;
    align-items: center;
    justify-content: center;
  }
  .wordmark {
    font-weight: 500;
    white-space: nowrap;
  }
  .card-front .wordmark { color: var(--paper); font-size: 54px; }

  .card-back {
    top: 476px;
    background: var(--paper);
  }
  .card-back .wordmark {
    position: absolute;
    right: 44px;
    top: 44px;
    color: var(--brand-sky);
    font-size: 32px;
  }
  .divider {
    position: absolute;
    left: 250px;
    right: 40px;
    top: 196px;
    height: 1.5px;
    background: var(--rule-blue);
  }
  .edge-tab {
    position: absolute;
    left: -8px;
    top: 186px;
    width: 18px;
    height: 44px;
    border-radius: 8px;
    background: var(--ink-blue);
  }
  .holder {
    position: absolute;
    left: 42px;
    top: 160px;
  }
  .holder-name {
    color: var(--ink-blue);
    font-weight: 600;
    font-size: 25px;
    line-height: 1.1;
  }
  .holder-role {
    color: var(--muted-grey);
    font-size: 16px;
    margin-top: 2px;
  }
  .contact-list {
    position: absolute;
    right: 36px;
    top: 218px;
    list-style: none;
    text-align: right;
  }
  .contact-list li {
    display: flex;
    align-items: center;
    justify-content: flex-end;
    gap: 12px;
    color: var(--text-grey);
    font-size: 15px;
    line-height: 22px;
  }
  .contact-list svg { width: 11px; height: 11px; fill: var(--ink-blue); }
</style>
</head>
<body>
  <section class="card card-front" aria-label="Card front">
    <div class="wordmark">Hartwell Connect</div>
  </section>

  <section class="card card-back" aria-label="Card back">
    <div class="wordmark">Hartwell Connect</div>
    <div class="divider"></div>
    <div class="edge-tab"></div>
    <div class="holder">
      <div class="holder-name">Rhys Calloway</div>
      <div class="holder-role">Director</div>
    </div>
    <ul class="contact-list">
      <li>0455218390
        <svg viewBox="0 0 24 24" aria-hidden="true"><path d="M6.6 10.8a15.1 15.1 0 0 0 6.6 6.6l2.2-2.2c.3-.3.7-.4 1-.2 1.1.4 2.3.6 3.6.6.6 0 1 .4 1 1V20c0 .6-.4 1-1 1A17 17 0 0 1 3 4c0-.6.4-1 1-1h3.5c.6 0 1 .4 1 1 0 1.3.2 2.5.6 3.6.1.3 0 .7-.2 1z"/></svg>
      </li>
      <li>hello@hartwellconnect.com.au
        <svg viewBox="0 0 24 24" aria-hidden="true"><path d="M2 5h20v14H2zm2 2v.5l8 5 8-5V7zm0 2.8V17h16V9.8l-8 5z"/></svg>
      </li>
      <li>www.hartwellconnect.com.au
        <svg viewBox="0 0 24 24" aria-hidden="true"><circle cx="12" cy="12" r="10"/></svg>
      </li>
    </ul>
  </section>
</body>
</html>
```